rl ironcraft business card metallic look

revamp the existing design but want card to have a metalic look to it

Target Market(s)

construction industry

Industry/Entity Type

constrction

Contact Information for Business Card

front of card RL Ironcraft, phone 4163920857, email rl.ironcraftt@quellmail.example and instagram account; rl_ironcraft_

Font styles to use
Other font styles liked:
• masculine

Colors

Designer to choose only greyscale colors for use in the design.

Requirements
Must have
• back side RL Ironcraft then a list of everything : Siding, ACM Panels, Standing Seam,Soffit, Fascia, Gutters,Metal,Alu,inum, Viynyl, Metal Roofs and roof repairs
Nice to have
• I would like to keep the look of the existing card with the metal grids on the front
Should not have
• Need a design in two days

```html
<!DOCTYPE html>
<html lang="en">
<head>
<meta charset="utf-8">
<title>RL Ironcraft – Business Card</title>
<link href="https://fonts.googleapis.com/css2?family=Montserrat:wght@500;800&display=swap" rel="stylesheet">
<style>
  :root {
    --backdrop: #bdbdbd;
    --steel-dark: #1c1c1a;
    --steel-mid: #4a4b47;
    --steel-light: #d9dad6;
    --steel-flare: #f4f4f0;
    --ink-light: #ececec;
    --ink-soft: #cfcfcf;
  }
  * { margin: 0; padding: 0; box-sizing: border-box; }
  html, body { width: 1200px; height: 920px; overflow: hidden; }
  body {
    background: var(--backdrop);
    font-family: "Montserrat", sans-serif;
    position: relative;
  }
  .card {
    position: absolute;
    top: 200px;
    width: 500px;
    height: 500px;
    border-radius: 4px;
    background:
      linear-gradient(115deg,
        transparent 42%,
        rgba(244,244,240,0.25) 52%,
        rgba(244,244,240,0.85) 60%,
        rgba(217,218,214,0.6) 66%,
        transparent 78%),
      linear-gradient(160deg, var(--steel-dark) 0%, var(--steel-mid) 55%, var(--steel-dark) 100%);
    color: var(--ink-light);
    overflow: hidden;
    box-shadow: 0 10px 24px rgba(0,0,0,0.25);
  }
  .card--back { left: 60px; }
  .card--front { left: 640px; }
  .brand {
    position: absolute;
    left: 0; right: 0;
    text-align: center;
    font-weight: 800;
    color: var(--ink-light);
    line-height: 1;
  }
  .brand__initials { display: block; font-size: 96px; letter-spacing: 4px; }
  .brand__word { display: block; font-size: 38px; letter-spacing: 2px; margin-top: 4px; }
  .card--back .brand { top: 110px; }
  .card--front .brand { top: 150px; }
  .services {
    position: absolute;
    top: 300px;
    left: 50px; right: 50px;
    text-align: center;
    font-size: 14px;
    font-weight: 500;
    line-height: 1.6;
    text-transform: uppercase;
    color: var(--ink-soft);
    letter-spacing: 0.5px;
  }
  .contacts {
    position: absolute;
    top: 340px;
    left: 0; right: 0;
    list-style: none;
    display: flex;
    flex-direction: column;
    align-items: center;
    gap: 10px;
    font-size: 16px;
    font-weight: 500;
  }
  .contacts li { display: flex; align-items: center; gap: 10px; }
  .contacts svg { width: 16px; height: 16px; flex: none; }
</style>
</head>
<body>
  <section class="card card--back" aria-label="Card back">
    <h2 class="brand"><span class="brand__initials">RL</span><span class="brand__word">IRONCRAFT</span></h2>
    <p class="services">Sliding, ACM Panels, Standing Seam, Soffit, Fascia, Gutters, Metal, Alu,inum, Viynyl, Metal Roofs and Roof Repairs</p>
  </section>

  <section class="card card--front" aria-label="Card front">
    <h1 class="brand"><span class="brand__initials">RL</span><span class="brand__word">IRONCRAFT</span></h1>
    <ul class="contacts">
      <li>
        <svg viewBox="0 0 16 16" aria-hidden="true"><path fill="#ececec" d="M3 2h3l1 3-2 1a8 8 0 0 0 5 5l1-2 3 1v3c0 1-1 1-1 1C7 14 2 9 2 3c0 0 0-1 1-1z"/></svg>
        <span>416 - 392 - 0857</span>
      </li>
      <li>
        <svg viewBox="0 0 16 16" aria-hidden="true"><rect x="1.5" y="3.5" width="13" height="9" fill="none" stroke="#ececec"/><path d="M1.5 3.5 8 9l6.5-5.5" fill="none" stroke="#ececec"/></svg>
        <span>rl.ironcraftt@quellmail.example</span>
      </li>
      <li>
        <svg viewBox="0 0 16 16" aria-hidden="true"><circle cx="8" cy="8" r="6.5" fill="none" stroke="#ececec" stroke-width="1.4"/></svg>
        <span>rl_ironcraft_</span>
      </li>
    </ul>
  </section>
</body>
</html>
```